Belvanta - Awnings & Outdoor Blinds

We need a brochure design for out Australia based Awnings & Outdoor Blinds company.

We require 2 templates:

1. Product Specific. (For One Product) - Single or Double Sided A4
Must Include:
Our Logo, Product Description, Pictures,Product Features & Benefits (in point form) & Our Contact Details (Phone & Website).

2.Product Range (Our Full Range) - 8 Page A4 (2x A3 Folded In Half Printed Both Sides).
Must Include:
Page 1 - Front Cover - Title (Product Range) Cover With Our Logo & Photo/s.
Page 2 - About Us, Why Us & Warranty Information.
Page 3 - A Gallery (Just Photos Showcasing Our Work)
Page 4 - 3 Products Per Page (Image/s, Product Title & Brief Description).
Page 5 - 3 Products Per Page (Image/s, Product Title & Brief Description).
Page 6 - 3 Products Per Page (Image/s, Product Title & Brief Description).
Page 7 - 3 Products Per Page (Image/s, Product Title & Brief Description).
Page 8 - Back Cover with our Contact Details (Phone, Website & Logo).

We are just looking for templates we will fill in all the content, needs to be easy to customise (change photos/text etc).

For more info on what we do: http://site7305.example-builder.com/belvanta

Requirements
Nice to have
• Nice to have the product pages 4 - 7 not as identical layout.

Nice to be in our colours Red, White, Black, Light Grey. (See Logo Variations - Logo is the top one).

```html
<!DOCTYPE html>
<html lang="en">
<head>
<meta charset="utf-8">
<title>Belvanta – Product Flyer Templates</title>
<link rel="stylesheet" href="https://fonts.googleapis.com/css2?family=Mulish:wght@300;400;600;700&display=swap">
<style>
:root{
  --red:#e31b23;
  --white:#ffffff;
  --ring:#c9c9c9;
  --grey-band:#c4c4c4;
  --text-dark:#1e1e1e;
  --text-light:#f2f2f2;
  --title-grey:#6d6d6d;
  --panel-light-top:#f4f4f4;
  --panel-light-bottom:#ffffff;
  --panel-dark:#4a4a4c;
  --tagline:#8a8a8a;
}
*{margin:0;padding:0;box-sizing:border-box}
html,body{width:1200px;height:844px;overflow:hidden;background:var(--white)}
body{position:relative;font-family:"Mulish",Arial,sans-serif}

.flyer{
  position:absolute;top:24px;width:597px;height:845px;
  transform:scale(0.9494);transform-origin:top left;overflow:hidden;
}
.flyer--light{left:17px;background:linear-gradient(180deg,var(--panel-light-top) 45%,var(--panel-light-bottom) 100%)}
.flyer--dark{left:614px;background:var(--panel-dark)}

.hero-photo{
  position:absolute;left:0;top:0;width:597px;height:380px;
  background:linear-gradient(180deg,#b9c3d1 0%,#a49c93 38%,#5d5348 55%,#8fa3ad 72%,#5fa8c2 82%,#c8ccd0 100%);
}
.header-bands{position:absolute;left:0;top:0;width:597px;height:460px}

.title-badge{
  position:absolute;left:202px;top:278px;width:200px;height:200px;border-radius:50%;
  background:var(--ring);display:flex;align-items:center;justify-content:center;
}
.title-badge__inner{
  width:176px;height:176px;border-radius:50%;
  background:radial-gradient(circle at 50% 40%,#ffffff 55%,#ececec 100%);
  display:flex;flex-direction:column;align-items:center;justify-content:center;
  color:var(--title-grey);line-height:1;
}
.title-badge__line1{font-weight:300;font-size:34px;letter-spacing:.5px}
.title-badge__line2{font-weight:600;font-size:34px;margin-top:4px}

.intro{position:absolute;left:27px;top:490px;width:290px}
.intro__heading{color:var(--red);font-weight:700;font-size:29px;line-height:1.1;margin-bottom:4px}
.intro__text{font-size:12px;line-height:15px}
.flyer--light .intro__text,.flyer--light .features{color:var(--text-dark)}
.flyer--dark .intro__text,.flyer--dark .features{color:var(--text-light)}

.features{position:absolute;left:33px;top:585px;list-style:none;font-size:12px;line-height:18.3px}
.features li{position:relative;padding-left:10px}
.features li::before{
  content:"";position:absolute;left:0;top:5px;width:8px;height:8px;border-radius:50%;background:var(--red);
}
.features li::after{
  content:"";position:absolute;left:2.6px;top:6.6px;width:2px;height:3.5px;
  border:solid var(--white);border-width:0 1.2px 1.2px 0;transform:rotate(40deg);
}

.gallery-circle{position:absolute;border-radius:50%;background:var(--white);display:flex;align-items:center;justify-content:center;box-shadow:0 1px 4px rgba(0,0,0,.18)}
.gallery-circle__photo{border-radius:50%}
.gallery-circle--house{left:317px;top:475px;width:158px;height:158px;z-index:1}
.gallery-circle--house .gallery-circle__photo{width:136px;height:136px;background:linear-gradient(180deg,#a7c3e0 0%,#e9ecef 45%,#6f8f4a 75%,#4f6a35 100%)}
.gallery-circle--lounge{left:432px;top:530px;width:146px;height:146px;z-index:2}
.gallery-circle--lounge .gallery-circle__photo{width:124px;height:124px;background:linear-gradient(180deg,#e8e8e8 0%,#8c98a4 40%,#d8d4cc 62%,#5a5a5a 100%)}
.gallery-circle--room{left:342px;top:590px;width:136px;height:136px;z-index:3}
.gallery-circle--room .gallery-circle__photo{width:116px;height:116px;background:linear-gradient(135deg,#d9432a 0%,#e8d64a 45%,#f0e68a 65%,#8a5a33 100%)}

.brand-card{
  position:absolute;left:330px;top:720px;width:264px;height:100px;background:var(--white);
  box-shadow:0 3px 6px rgba(0,0,0,.25);display:flex;flex-direction:column;justify-content:center;padding-left:26px;
}
.brand-card__name{display:flex;align-items:center;gap:10px;font-weight:600;font-size:34px;color:var(--text-dark);line-height:1}
.brand-card__dot{width:22px;height:22px;border-radius:50%;background:var(--red)}
.brand-card__tagline{font-size:8px;letter-spacing:2.6px;color:var(--tagline);margin:6px 0 0 32px}
</style>
</head>
<body>

<!-- Light variant -->
<section class="flyer flyer--light">
  <div class="hero-photo" role="img" aria-label="Evening view of a modern home with pool, lit interiors and a retractable awning over the patio"></div>
  <svg class="header-bands" viewBox="0 0 597 460" aria-hidden="true">
    <polygon points="0,345 597,345 597,410 300,430 0,410" fill="var(--red)"/>
    <polygon points="0,410 300,430 597,410 597,425 300,448 0,425" fill="var(--grey-band)"/>
  </svg>
  <div class="title-badge"><div class="title-badge__inner"><span class="title-badge__line1">PRODUCT</span><span class="title-badge__line2">NAME</span></div></div>
  <div class="intro">
    <h2 class="intro__heading">Duis commodo</h2>
    <p class="intro__text">Lorem ipsum dolor sit amet, consectetur adipiscing elit. Quisque iaculis id erat ac porta. Duis commodo sem eu nibh venenatis faucibus.</p>
  </div>
  <ul class="features">
    <li>Lorem ipsum dolor sit amet</li><li>Pellentesque ultrices aliquet</li><li>Quisque porttitor dictum tortor</li><li>Integer eu fringilla</li><li>Duis tristique nunc vitae</li><li>Lorem ipsum dolor sit amet</li><li>Pellentesque ultrices aliquet</li><li>Quisque porttitor dictum tortor</li><li>Integer eu fringilla</li><li>Duis tristique nunc vitae</li><li>Pellentesque ultrices aliquet</li><li>Quisque porttitor dictum tortor</li>
  </ul>
  <div class="gallery-circle gallery-circle--house"><div class="gallery-circle__photo" role="img" aria-label="White weatherboard house with garden"></div></div>
  <div class="gallery-circle gallery-circle--lounge"><div class="gallery-circle__photo" role="img" aria-label="Living room with sofa and large window"></div></div>
  <div class="gallery-circle gallery-circle--room"><div class="gallery-circle__photo" role="img" aria-label="Room with yellow roller blind"></div></div>
  <div class="brand-card">
    <div class="brand-card__name"><span class="brand-card__dot"></span>Belvanta</div>
    <div class="brand-card__tagline">Awnings &amp; Outdoor Blinds</div>
  </div>
</section>

<!-- Dark variant -->
<section class="flyer flyer--dark">
  <div class="hero-photo" role="img" aria-label="Evening view of a modern home with pool, lit interiors and a retractable awning over the patio"></div>
  <svg class="header-bands" viewBox="0 0 597 460" aria-hidden="true">
    <polygon points="0,345 597,345 597,410 300,430 0,410" fill="var(--red)"/>
    <polygon points="0,410 300,430 597,410 597,425 300,448 0,425" fill="var(--grey-band)"/>
  </svg>
  <div class="title-badge"><div class="title-badge__inner"><span class="title-badge__line1">PRODUCT</span><span class="title-badge__line2">NAME</span></div></div>
  <div class="intro">
    <h2 class="intro__heading">Duis commodo</h2>
    <p class="intro__text">Lorem ipsum dolor sit amet, consectetur adipiscing elit. Quisque iaculis id erat ac porta. Duis commodo sem eu nibh venenatis faucibus.</p>
  </div>
  <ul class="features">
    <li>Lorem ipsum dolor sit amet</li><li>Pellentesque ultrices aliquet</li><li>Quisque porttitor dictum tortor</li><li>Integer eu fringilla</li><li>Duis tristique nunc vitae</li><li>Lorem ipsum dolor sit amet</li><li>Pellentesque ultrices aliquet</li><li>Quisque porttitor dictum tortor</li><li>Integer eu fringilla</li><li>Duis tristique nunc vitae</li><li>Pellentesque ultrices aliquet</li><li>Quisque porttitor dictum tortor</li>
  </ul>
  <div class="gallery-circle gallery-circle--house"><div class="gallery-circle__photo" role="img" aria-label="White weatherboard house with garden"></div></div>
  <div class="gallery-circle gallery-circle--lounge"><div class="gallery-circle__photo" role="img" aria-label="Living room with sofa and large window"></div></div>
  <div class="gallery-circle gallery-circle--room"><div class="gallery-circle__photo" role="img" aria-label="Room with yellow roller blind"></div></div>
  <div class="brand-card">
    <div class="brand-card__name"><span class="brand-card__dot"></span>Belvanta</div>
    <div class="brand-card__tagline">Awnings &amp; Outdoor Blinds</div>
  </div>
</section>

</body>
</html>
```